VeloRoot Sample Packaging Design

We need a design - with assistance on logo and colours - of a box containing sample sachets of a new natural sports supplement for endurance athletes.
We have an idea of logo and colours but would like input, ideas and assistance to create a cool new brand.

The product is based on natural beetroot powder which is scientifically backed to improve sports performance.
We like clean minimal branding that looks scientific - such as Kestrel Fuel, Stack Grains, Cortex Well Max and TuL Omni Drive sachets.

Attached is the type of package we will be using with matt black sachets, so clean white with potentially a beetroot colour (hex 691a40??) and grey (a3b2c2??) but we would like your professional and creative input.

I have attached a rough logo mock up of the logo I designed, happy for you to develop this by making it a bit cleaner (left edges angled or curved maybe- change font also maybe??) or your own ideas if clean, simple and effective. I based mine off the Far Meridian logo and PB works well with VeloRoot and Personal Best.

The final design should be clean, minimalist, high end sports supplement with a science and natural beetroot feel.
Box size: 300mm x 130mm x 14mm

Target Market(s)

Elite athletes and professionals wanting natural and science-backed supplements that work. Probably mainly men.
The customers are long distance sportspeople and NOT bodybuilders! Including triathletes, cyclists, long distance runners and swimmers.
The brand must also appeal to club level athletes and weekend warriors (but this should be easy if it's targeted at elite level first)

Industry/Entity Type

Supplement

Font styles to use
Sans Serif

Colors

Designer to choose colors to be used in the design.

Requirements
Must have
• - New logo (I like the Far Meridian logo but open to new ideas!)
• - Clean, scientific look with a twist of "I'm natural and not full of sports supplement junk!!"
• - A shade of beetroot red/purple as the signature colour, without looking too feminine.
• - Our slogan is "Beat your best"
Should not have
• A bodybuilder look.

```html
<!DOCTYPE html>
<html lang="en">
<head>
<meta charset="utf-8">
<title>VeloRoot – Beetroot Raw Powder Sachet</title>
<link rel="stylesheet" href="https://fonts.googleapis.com/css2?family=Questrial&family=Montserrat:wght@500&display=swap">
<style>
  :root {
    --stage: #d4d4d4;
    --card: #ffffff;
    --frame: #555555;
    --ink: #3a3a3a;
    --ink-soft: #4b4b4b;
    --beet: #c1184d;
    --beet-light: #e8506b;
    --leaf: #8c9b3b;
    --rule: #6a6a6a;
    --mist: #e9e9eb;
  }
  * { box-sizing: border-box; margin: 0; padding: 0; }
  html, body { width: 844px; height: 1200px; overflow: hidden; background: var(--stage); }
  .sachet {
    position: absolute; left: 43px; top: 52px; width: 758px; height: 1102px;
    background: var(--card); border: 1.5px solid var(--frame); overflow: hidden;
    font-family: "Questrial", sans-serif; color: var(--ink);
  }
  .science-backdrop {
    position: absolute; left: 0; top: 300px; width: 758px; height: 802px;
    background: radial-gradient(ellipse 60% 55% at 55% 55%, var(--mist) 0%, rgba(240,240,242,0.6) 45%, rgba(255,255,255,0) 80%);
  }
  .claims { position: absolute; left: 58px; top: 72px; list-style: none; }
  .claims li {
    display: flex; align-items: center; gap: 8px;
    font-size: 24px; line-height: 43.5px; color: var(--ink);
  }
  .claims svg { width: 17px; height: 17px; flex: none; }
  .brand-mark {
    position: absolute; left: 259px; top: 313px; width: 240px; height: 240px;
    border-radius: 50%; background: var(--beet);
  }
  .brand-name {
    position: absolute; left: 0; width: 758px; top: 588px; text-align: center;
    font-size: 72px; line-height: 1; color: var(--ink-soft); letter-spacing: 1px;
  }
  .rule { position: absolute; left: 79px; width: 599px; height: 1.5px; background: var(--rule); }
  .rule.top { top: 680px; }
  .rule.bottom { top: 832px; }
  .product-name {
    position: absolute; left: 202px; top: 696px;
    font-family: "Montserrat", sans-serif; font-weight: 500;
    font-size: 30px; line-height: 44.5px; letter-spacing: 3.5px; text-transform: uppercase;
    color: #1f1f1f; transform: scaleX(1.12); transform-origin: left;
  }
  .product-name .accent { color: var(--beet); }
  .beet-illustration {
    position: absolute; left: 488px; top: 696px; width: 117px; height: 123px;
    border-radius: 50% 50% 45% 45%;
    background: linear-gradient(90deg, var(--beet) 0%, var(--beet) 50%, var(--beet-light) 100%);
  }
  .usage { position: absolute; top: 973px; left: 191px; display: flex; gap: 22px; }
  .usage-item { display: flex; align-items: flex-start; gap: 5px; font-size: 18px; line-height: 19px; color: var(--ink); }
  .usage-icon { width: 44px; height: 44px; flex: none; }
</style>
</head>
<body>
  <main class="sachet">
    <div class="science-backdrop" role="img" aria-label="Faint grey molecule network and hexagon pattern"></div>

    <ul class="claims">
      <li><svg viewBox="0 0 20 20" aria-hidden="true"><circle cx="10" cy="10" r="10" fill="var(--leaf)"/><path d="M5 10.5l3.2 3.2L15 6.8" stroke="#fff" stroke-width="2.6" fill="none" stroke-linecap="round" stroke-linejoin="round"/></svg>100% Pure</li>
      <li><svg viewBox="0 0 20 20" aria-hidden="true"><circle cx="10" cy="10" r="10" fill="var(--leaf)"/><path d="M5 10.5l3.2 3.2L15 6.8" stroke="#fff" stroke-width="2.6" fill="none" stroke-linecap="round" stroke-linejoin="round"/></svg>Gluten Free</li>
      <li><svg viewBox="0 0 20 20" aria-hidden="true"><circle cx="10" cy="10" r="10" fill="var(--leaf)"/><path d="M5 10.5l3.2 3.2L15 6.8" stroke="#fff" stroke-width="2.6" fill="none" stroke-linecap="round" stroke-linejoin="round"/></svg>Excellent Taste</li>
    </ul>

    <div class="brand-mark" aria-hidden="true"></div>
    <h1 class="brand-name">VeloRoot</h1>

    <div class="rule top"></div>
    <p class="product-name">Naturally<br><span class="accent">Beetroot</span><br>Raw Powder</p>
    <div class="beet-illustration" role="img" aria-label="Beetroot illustration, whole root with green leaves and a sliced half showing rings"></div>
    <div class="rule bottom"></div>

    <div class="usage">
      <div class="usage-item">
        <svg class="usage-icon" viewBox="0 0 44 44" aria-hidden="true">
          <circle cx="22" cy="22" r="22" fill="var(--beet)"/>
          <rect x="14" y="11" width="16" height="22" rx="1.5" fill="none" stroke="#fff" stroke-width="1.8"/>
          <path d="M14 15h16M14 29h16" stroke="#fff" stroke-width="1.2"/>
        </svg>
        <span>1 Serving<br>Per Sachet</span>
      </div>
      <div class="usage-item">
        <svg class="usage-icon" viewBox="0 0 44 44" aria-hidden="true">
          <circle cx="22" cy="22" r="22" fill="var(--beet)"/>
          <path d="M13 11h18l-2.5 22h-13z" fill="none" stroke="#fff" stroke-width="1.8" stroke-linejoin="round"/>
          <path d="M14.5 19q3.8-2 7.5 0t7.5 0" fill="none" stroke="#fff" stroke-width="1.4"/>
        </svg>
        <span>Just Add Water,<br>Shake &amp; Go!</span>
      </div>
    </div>
  </main>
</body>
</html>
```